New Card

Photography business
I want a sleek simple card that screams rich and classy. Black/Gold or silver font. No photos or images but would love a new logo When I hand someone my card I want compliments
Updates
My fiancé reminded me in 5 short months my name will change so I have changed my name to Colleen Marwick
Also my BRAND is Lantern Bloom Photography, not my name. Thanks
Industry/Entity Type
Business
Contact Information for Business Card
Lantern Bloom Photography
Colleen Marwick-owner
482 W. Thornbury Rd.
Willowmere, NJ 00000
(555)555-0142
colleen@lanternbloomstudio.example
Look and feel
Each slider illustrates characteristics of the customer's brand and the style your logo design should communicate.

```html
<!DOCTYPE html>
<html lang="en">
<head>
<meta charset="utf-8">
<title>Lantern Bloom Photography – Business Card</title>
<link rel="stylesheet" href="https://fonts.googleapis.com/css2?family=Marcellus&family=Montserrat:wght@300;400&display=swap">
<style>
  :root {
    --canvas-bg: #e9e4dc;
    --card-center: #2b2b2b;
    --card-edge: #070707;
    --gold: #c9a24a;
    --silver: #d6d6d6;
    --muted: #a8a8a8;
  }
  * { margin: 0; padding: 0; box-sizing: border-box; }
  html, body {
    width: 1200px;
    height: 784px;
    overflow: hidden;
    background: var(--canvas-bg);
  }
  .sheet {
    width: 1200px;
    height: 784px;
    display: flex;
    align-items: center;
    justify-content: center;
    gap: 40px;
  }
  .card {
    width: 540px;
    height: 309px;
    border-radius: 4px;
    background: radial-gradient(ellipse at 50% 38%, var(--card-center) 0%, #161616 45%, var(--card-edge) 100%);
    box-shadow: 0 10px 24px rgba(0, 0, 0, 0.25);
    position: relative;
    color: var(--silver);
    text-align: center;
    overflow: hidden;
  }
  .card--back .owner-name {
    position: absolute;
    top: 52px;
    left: 0; right: 0;
    font-family: "Marcellus", serif;
    font-size: 19px;
    color: var(--gold);
    letter-spacing: 0.3px;
  }
  .card--back .owner-title {
    position: absolute;
    top: 78px;
    left: 0; right: 0;
    font-family: "Montserrat", sans-serif;
    font-weight: 300;
    font-size: 11px;
    color: var(--muted);
  }
  .card--back .contact {
    position: absolute;
    top: 128px;
    left: 0; right: 0;
    font-family: "Montserrat", sans-serif;
    font-weight: 300;
    line-height: 1.35;
  }
  .contact .phone { font-size: 19px; color: var(--silver); }
  .contact .email,
  .contact .address { font-size: 13px; color: var(--silver); }
  .card--front .brand {
    position: absolute;
    top: 50%;
    left: 0; right: 0;
    transform: translateY(-50%);
    display: flex;
    align-items: center;
    justify-content: center;
    gap: 14px;
  }
  .brand-dot {
    width: 18px;
    height: 18px;
    border-radius: 50%;
    background: var(--gold);
  }
  .brand-name {
    font-family: "Marcellus", serif;
    font-size: 26px;
    color: var(--gold);
    letter-spacing: 0.5px;
  }
</style>
</head>
<body>
  <main class="sheet">
    <section class="card card--back" aria-label="Card back">
      <p class="owner-name">Colleen Marwick</p>
      <p class="owner-title">Owner</p>
      <div class="contact">
        <p class="phone">(555)555-0142</p>
        <p class="email">colleen@lanternbloomstudio.example</p>
        <p class="address">482 W. Thornbury Rd. Willowmere, NJ 00000</p>
      </div>
    </section>
    <section class="card card--front" aria-label="Card front">
      <div class="brand">
        <span class="brand-dot"></span>
        <span class="brand-name">Lantern Bloom Photography</span>
      </div>
    </section>
  </main>
</body>
</html>
```